Business Card Design

Cake decorating business in a small town in Australia. looking for a style that is fresh with a touch of vintage/country. liking these ideas, timber backgrounds, chalkboards, bunting, flowers and cake elements (rolling pins, cupcakes, cake stands, etc.) would consider a shot saying/statement. would like the back of the card to have wording "Specialising in delectable treats for all your special occasions" - wedding cakes - birthday cakes - special occasion cakes - novelty cakes - cupcakes, cookies, slices and cake pops. maybe incorporate a cake in design on back page. attached are a few of my favourite cakes and the start of a card design I liked.

Industry/Entity Type

Business

Contact Information for Business Card

Marla's Sugarcrest Kitchen 0438 056 969Find me on (Linkbook Logo)

Requirements
Nice to have
• timber, some of my designs, chalkboard, baking utensils
Should not have
• no red font

```html
<!DOCTYPE html>
<html lang="en">
<head>
<meta charset="utf-8">
<title>Marla's Sugarcrest Kitchen – Business Card</title>
<link rel="stylesheet" href="https://fonts.googleapis.com/css2?family=Arvo:wght@400;700&display=swap">
<style>
  :root {
    --page: #e9e6e2;
    --timber-light: #efedf1;
    --timber-mid: #dedbe3;
    --timber-shade: #c4bfcb;
    --timber-seam: rgba(150, 142, 160, .55);
    --chalk: #2b2420;
    --chalk-line: #f4f1ec;
    --white: #ffffff;
    --pink: #e8559a;
    --green: #93d17c;
    --teal: #5fc59a;
    --peach: #eab98c;
    --cake-pink: #ee6aa8;
    --cake-green: #7fd38a;
  }
  * { box-sizing: border-box; margin: 0; padding: 0; }
  html, body { width: 1200px; height: 1000px; overflow: hidden; }
  body {
    background: var(--page);
    font-family: "Arvo", Georgia, serif;
    display: flex;
    align-items: center;
    justify-content: center;
    gap: 50px;
  }
  .card {
    position: relative;
    width: 540px;
    height: 310px;
    box-shadow: 0 6px 18px rgba(0,0,0,.18);
    overflow: hidden;
  }
  .card__timber {
    position: absolute; inset: 0;
    background:
      repeating-linear-gradient(180deg, transparent 0 36px, var(--timber-seam) 36px 38px),
      repeating-linear-gradient(90deg, transparent 0 173px, rgba(150,142,160,.3) 173px 175px),
      linear-gradient(160deg, var(--timber-light), var(--timber-mid) 55%, var(--timber-shade));
  }
  .card__board {
    position: absolute;
    left: 50%; top: 50%;
    width: 450px; height: 250px;
    transform: translate(-50%, -50%);
  }
  .card__content {
    position: absolute;
    left: 50%; top: 50%;
    width: 350px; height: 196px;
    transform: translate(-50%, -50%);
    color: var(--white);
    text-align: center;
  }

  /* back */
  .back__statement {
    font-weight: 700;
    font-size: 17px;
    line-height: 1.3;
    margin-top: 14px;
  }
  .back__services { margin-top: 14px; font-size: 13px; line-height: 1.8; }
  .back__row { display: flex; justify-content: space-between; padding: 0 4px; }
  .svc--green { color: var(--green); }
  .svc--teal { color: var(--teal); }
  .svc--pink { color: var(--pink); }
  .svc--peach { color: var(--peach); }
  .back__cherry-line {
    display: flex; align-items: center; justify-content: center; gap: 8px;
  }
  .back__cherry {
    flex: none;
    width: 14px; height: 14px;
    border-radius: 50%;
    background: var(--pink);
  }

  /* front */
  .front__name {
    font-weight: 700;
    font-size: 21px;
    margin-top: 14px;
    letter-spacing: .3px;
  }
  .front__phone {
    color: var(--pink);
    font-size: 15px;
    text-align: left;
    margin: 10px 0 0 6px;
    letter-spacing: 1px;
  }
  .front__cake {
    position: absolute;
    left: 30px; top: 92px;
    width: 100px; height: 80px;
    border-radius: 6px;
    background: linear-gradient(var(--cake-green) 0 40%, var(--cake-pink) 40% 100%);
  }
  .front__social {
    position: absolute;
    right: 6px; bottom: 30px;
    display: flex; align-items: center; gap: 8px;
    color: var(--pink);
    font-size: 14px;
  }
  .front__social-mark {
    width: 11px; height: 11px; background: var(--pink);
  }
</style>
</head>
<body>

  <section class="card card--back">
    <div class="card__timber" role="img" aria-label="Whitewashed timber plank background"></div>
    <svg class="card__board" viewBox="-10 -10 460 260" aria-hidden="true">
      <path d="M30,10 Q220,-6 410,10 A22,22 0 0 0 430,32 Q446,120 430,208 A22,22 0 0 0 410,230 Q220,246 30,230 A22,22 0 0 0 10,208 Q-6,120 10,32 A22,22 0 0 0 30,10 Z" fill="var(--chalk)"/>
      <path transform="translate(220 120) scale(.94 .9) translate(-220 -120)" d="M30,10 Q220,-6 410,10 A22,22 0 0 0 430,32 Q446,120 430,208 A22,22 0 0 0 410,230 Q220,246 30,230 A22,22 0 0 0 10,208 Q-6,120 10,32 A22,22 0 0 0 30,10 Z" fill="none" stroke="var(--chalk-line)" stroke-width="2" stroke-dasharray="6 4"/>
    </svg>
    <div class="card__content">
      <p class="back__statement">Specialising in delectable<br>treats for all your special occasions</p>
      <div class="back__services">
        <p class="back__row">
          <span class="svc--green">wedding cakes</span>
          <span class="svc--teal">birthday cakes</span>
          <span class="svc--green">novelty cakes</span>
        </p>
        <p class="svc--pink">special occasion cakes</p>
        <p class="back__cherry-line svc--peach">
          <span class="back__cherry" role="img" aria-label="Cherry illustration"></span>
          <span>cupcakes, cookies, slices and cake pops</span>
        </p>
      </div>
    </div>
  </section>

  <section class="card card--front">
    <div class="card__timber" role="img" aria-label="Whitewashed timber plank background"></div>
    <svg class="card__board" viewBox="-10 -10 460 260" aria-hidden="true">
      <path d="M30,10 Q220,-6 410,10 A22,22 0 0 0 430,32 Q446,120 430,208 A22,22 0 0 0 410,230 Q220,246 30,230 A22,22 0 0 0 10,208 Q-6,120 10,32 A22,22 0 0 0 30,10 Z" fill="var(--chalk)"/>
      <path transform="translate(220 120) scale(.94 .9) translate(-220 -120)" d="M30,10 Q220,-6 410,10 A22,22 0 0 0 430,32 Q446,120 430,208 A22,22 0 0 0 410,230 Q220,246 30,230 A22,22 0 0 0 10,208 Q-6,120 10,32 A22,22 0 0 0 30,10 Z" fill="none" stroke="var(--chalk-line)" stroke-width="2" stroke-dasharray="6 4"/>
    </svg>
    <div class="card__content">
      <h1 class="front__name">Marla's Sugarcrest Kitchen</h1>
      <p class="front__phone">0471 283 514</p>
      <div class="front__cake" role="img" aria-label="Illustrated layered cake with a cherry on a cake stand"></div>
      <p class="front__social">find me on <span>Linkbook</span><span class="front__social-mark"></span></p>
    </div>
  </section>

</body>
</html>
```